Business card design needed

We are a wine business involved in winemaking, broking and packaging on behalf of clients globally with the majority being Asian. The design should be quite traditional and classic with some red used, font used should be easily read.

Target Market(s)

Trade customers other business owners

Industry/Entity Type

Business

Contact Information for Business Card

Rosalind Thwaite
Meridale Wine Collective
PO Box 738, Fenwick Vale
South Australia 5187
Phone: +61 (0)455 982 317
Email: kvcellars@brightmail.example

Logo styles of interest
Lettermark Logo

```html
<!DOCTYPE html>
<html lang="en">
<head>
<meta charset="utf-8">
<title>Meridale Wine Collective – Business Card</title>
<link rel="stylesheet" href="https://fonts.googleapis.com/css2?family=Cinzel:wght@400;600&family=Open+Sans:wght@400&display=swap">
<style>
  :root {
    --backdrop: #5a534e;
    --card-white: #ffffff;
    --wine-red: #e00022;
    --ink: #111111;
    --rule: #b5b5b5;
    --on-red: #ffffff;
  }
  * { box-sizing: border-box; margin: 0; padding: 0; }
  html, body {
    width: 1200px; height: 1000px; overflow: hidden;
    background: var(--backdrop);
  }
  .card {
    position: absolute;
    left: 150px; top: 243px;
    width: 900px; height: 514px;
    background: var(--card-white);
    box-shadow: 0 6px 18px rgba(0,0,0,0.35);
    overflow: hidden;
  }
  .brand-name {
    position: absolute;
    top: 108px; left: 0; right: 0;
    text-align: center;
    font-family: "Cinzel", serif;
    font-weight: 400;
    font-size: 40px;
    letter-spacing: 2px;
    color: var(--wine-red);
  }
  .name-block {
    position: absolute;
    top: 248px; left: 210px; right: 210px;
    height: 64px;
    border-top: 1.5px solid var(--rule);
    border-bottom: 1.5px solid var(--rule);
    display: flex; align-items: center; justify-content: center;
  }
  .person-name {
    font-family: "Cinzel", serif;
    font-weight: 600;
    font-size: 26px;
    letter-spacing: 1px;
    color: var(--ink);
  }
  .contact-band {
    position: absolute;
    left: 0; right: 0; bottom: 0;
    height: 152px;
    background: var(--wine-red);
    color: var(--on-red);
    font-family: "Open Sans", sans-serif;
    font-size: 22px;
    letter-spacing: 0.5px;
    line-height: 32px;
    display: flex; justify-content: space-between;
    padding: 30px 62px 0 64px;
  }
  .contact-lines .label { display: inline-block; width: 100px; }
  .address { text-align: left; }
</style>
</head>
<body>
  <main class="card">
    <div class="brand-name">Meridale Wine Collective</div>

    <div class="name-block">
      <h1 class="person-name">ROSALIND THWAITE</h1>
    </div>

    <footer class="contact-band">
      <div class="contact-lines">
        <p><span class="label">Phone:</span>+61 (0)455 982 317</p>
        <p><span class="label">Email:</span>kvcellars@brightmail.example</p>
      </div>
      <address class="address" style="font-style: normal;">
        <p>PO Box 738, Fenwick Vale</p>
        <p>South Australia 5187</p>
      </address>
    </footer>
  </main>
</body>
</html>
```